Business Card Design Project

Thornwick Property Management

Our Business is residential property management, we therefore need a card that displays a professional image, but is clear and concise, and easy to read
Updates

We are committed now guys and girls, loving what we are seeing so far! 

Target Market(s)

Landlords, Rental Property Owners

Industry/Entity Type

Residential

Requirements
Must have
• Dale Thornwick - Principal
Fiona Thornwick - Director (Property Management)

PO Box 817
Pellworth SA 5193

Dale: 0490 367 258
Fiona: 0490 723 519

www.thornwickpropertymanagement.com.au
admin@thornwickpropertymanagement.com.au

Nice to have
• I would like the card to be double sided, white background on the information side and then colour on the reverse, in blue or black and incorporating our logo

```html
<!DOCTYPE html>
<html lang="en">
<head>
<meta charset="utf-8">
<title>Thornwick Property Management – Business Card</title>
<link rel="stylesheet" href="https://fonts.googleapis.com/css2?family=Open+Sans:wght@300;400;600;700&display=swap">
<style>
  :root {
    --page-bg: #e4e5e7;
    --card-white: #ffffff;
    --brand-blue: #0b5fa8;
    --brand-blue-light: #2a9ad6;
    --brand-blue-dark: #0a4f93;
    --ink-dark: #2f2f31;
    --ink-grey: #6b6c6f;
    --tab-dark: #3a3b3d;
  }
  * { box-sizing: border-box; margin: 0; padding: 0; }
  html, body {
    width: 1200px; height: 900px; overflow: hidden;
    background: var(--page-bg);
    font-family: "Open Sans", Arial, sans-serif;
  }
  .canvas {
    width: 1200px; height: 900px;
    display: flex; align-items: center; justify-content: center; gap: 30px;
  }
  .card {
    position: relative;
    width: 560px; height: 320px;
    overflow: hidden;
    box-shadow: 0 6px 18px rgba(0,0,0,0.18);
  }

  /* Information side */
  .card-front { background: var(--card-white); }
  .brand-mark {
    position: absolute; left: 30px; top: 26px;
    display: flex; align-items: center; gap: 10px;
  }
  .brand-square { width: 34px; height: 34px; background: var(--brand-blue); }
  .brand-name {
    font-weight: 700; font-size: 30px; line-height: 1;
    color: var(--ink-dark); letter-spacing: -0.5px;
  }
  .brand-sub {
    font-weight: 700; font-size: 11px; color: var(--ink-dark);
    margin-top: 3px;
  }
  .address {
    position: absolute; left: 34px; top: 92px;
    font-style: normal;
    font-weight: 300; font-size: 14px; line-height: 19px; color: var(--ink-grey);
  }
  .contact-list {
    position: absolute; left: 34px; top: 138px;
    list-style: none;
    font-weight: 300; font-size: 13px; line-height: 19px; color: var(--ink-grey);
  }
  .contact-list li { display: flex; align-items: center; gap: 8px; }
  .contact-icon { width: 11px; height: 11px; flex: none; }
  .people {
    position: absolute; right: 30px; bottom: 36px;
    text-align: right;
  }
  .person + .person { margin-top: 6px; }
  .person-name {
    font-weight: 600; font-size: 17px; color: var(--brand-blue); line-height: 1.15;
  }
  .person-role {
    font-weight: 300; font-size: 12px; color: var(--ink-grey); line-height: 1.35;
  }
  .footer-band { position: absolute; left: 0; bottom: 0; width: 560px; height: 20px; }

  /* Colour side */
  .card-back {
    background: radial-gradient(ellipse at 75% 35%, var(--brand-blue-light) 0%, var(--brand-blue) 55%, var(--brand-blue-dark) 100%);
  }
  .back-brand {
    position: absolute; right: 34px; bottom: 40px;
    display: flex; align-items: center; gap: 14px;
    color: var(--card-white); font-weight: 700;
  }
  .back-square { width: 56px; height: 56px; background: var(--card-white); flex: none; }
  .back-brand .name { font-size: 50px; line-height: 1; letter-spacing: -1px; }
  .back-brand .sub { font-size: 14px; margin-top: 2px; }
</style>
</head>
<body>
<main class="canvas">

  <section class="card card-front" aria-label="Business card information side">
    <div class="brand-mark">
      <span class="brand-square"></span>
      <div>
        <div class="brand-name">Thornwick</div>
        <div class="brand-sub">Property Management</div>
      </div>
    </div>

    <address class="address">
      PO Box 817<br>Pellworth SA 5193
    </address>

    <ul class="contact-list">
      <li>
        <svg class="contact-icon" viewBox="0 0 12 12"><path d="M2 1h2.5l1 3-1.5 1a6 6 0 0 0 3 3l1-1.5 3 1V10a1 1 0 0 1-1 1A9 9 0 0 1 1 2a1 1 0 0 1 1-1z" fill="var(--brand-blue)"/></svg>
        Dale: 0490 367 258
      </li>
      <li>
        <svg class="contact-icon" viewBox="0 0 12 12"><rect x="1" y="8" width="2" height="3" fill="var(--brand-blue)"/><rect x="4" y="6" width="2" height="5" fill="var(--brand-blue)"/><rect x="7" y="4" width="2" height="7" fill="var(--brand-blue)"/><rect x="10" y="2" width="2" height="9" fill="var(--brand-blue)"/></svg>
        Fiona: 0490 723 519
      </li>
      <li>
        <svg class="contact-icon" viewBox="0 0 12 12"><rect x="0.5" y="2.5" width="11" height="7" fill="none" stroke="var(--brand-blue)"/><path d="M0.5 2.5l5.5 4 5.5-4" fill="none" stroke="var(--brand-blue)"/></svg>
        admin@thornwickpropertymanagement.com.au
      </li>
      <li>
        <svg class="contact-icon" viewBox="0 0 12 12"><circle cx="6" cy="6" r="5.2" fill="none" stroke="var(--brand-blue)"/><ellipse cx="6" cy="6" rx="2.2" ry="5.2" fill="none" stroke="var(--brand-blue)"/><path d="M1 6h10" stroke="var(--brand-blue)"/></svg>
        www.thornwickpropertymanagement.com.au
      </li>
    </ul>

    <div class="people">
      <div class="person">
        <div class="person-name">Dale Thornwick</div>
        <div class="person-role">Principal</div>
      </div>
      <div class="person">
        <div class="person-name">Fiona Thornwick</div>
        <div class="person-role">Director (Property Management)</div>
      </div>
    </div>

    <svg class="footer-band" viewBox="0 0 560 20" preserveAspectRatio="none" aria-hidden="true">
      <rect x="0" y="12" width="440" height="4" fill="var(--brand-blue)"/>
      <path d="M440 16 L452 4 L560 4 L560 20 L0 20 L0 16 Z" fill="var(--tab-dark)"/>
      <rect x="0" y="16" width="440" height="4" fill="var(--card-white)"/>
    </svg>
  </section>

  <section class="card card-back" aria-label="Business card colour side">
    <div class="back-brand">
      <span class="back-square"></span>
      <div>
        <div class="name">Thornwick</div>
        <div class="sub">Property Management</div>
      </div>
    </div>
  </section>

</main>
</body>
</html>
```